Creative, Innovative PowerPoint Sales Deck Refresh needed

We are a technology firm in the Dallas, TX area and we need the powerpoint presentation used for our sales calls refreshed. This presentation is used in one of the first meetings we have with potential clients, so we want to make a memorable and positive impact - we want something that sets us apart from everyone else. We need 8 master slide templates created for our sales deck and a series of slides within the example sales deck need to be completely refreshed (slides 31-37 and 43 in the sample ppt file) We want a sales deck that is modern, innovative, creative, memorable and whimsical - NOT a typical boring "business" design. Colors should match or compliment the colors used in our logo. The logo in the footer of the attached sample ppt is old - it should be replaced with the newer logo attached. Please take a look at our website to get an idea of our culture and aesthetic www.quorbinlab.com
Updates

Project Deadline Extended
Reason: We have received several designs we like and we want our entire team to have time to give them full consideration before making a decision.

Target Market(s)

Business executives

Industry/Entity Type

Information Technology

Font styles to use
Sans Serif

Requirements
Must have
• Our logo and LedgerWave logo in footer
• Master Slide Templates
• Rework / redesign of slides 31-37 and 43
Nice to have
• We use Raleway font in a lot of our materials

```html
<!DOCTYPE html>
<html lang="en">
<head>
<meta charset="utf-8">
<title>Sales Deck Templates</title>
<link href="https://fonts.googleapis.com/css2?family=Raleway:wght@300;400;600;700;800&family=Open+Sans:wght@400;600&display=swap" rel="stylesheet">
<style>
:root{
  --navy:#1b5b8f;
  --navy-dark:#144a76;
  --orange:#f07123;
  --green:#6bb23f;
  --ink:#2c2c2c;
  --grey:#8a8f95;
  --light:#eef0f2;
  --rule:#dfe3e7;
  --white:#ffffff;
}
*{box-sizing:border-box;margin:0;padding:0}
html,body{width:1038px;height:1200px;overflow:hidden;background:#e9ebee}
body{font-family:"Open Sans",sans-serif;color:var(--ink)}
.deck{display:grid;grid-template-columns:repeat(3,343px);grid-auto-rows:196px;gap:4px 4px;padding:2px 0 0 0}
.slide{position:relative;background:var(--white);overflow:hidden;box-shadow:0 1px 2px rgba(0,0,0,.12)}

/* brand marks (text only) */
.brand{display:flex;align-items:center;gap:6px;font-family:"Raleway",sans-serif;font-weight:600;color:var(--ink)}
.brand .dot{width:14px;height:14px;border-radius:50%;background:var(--navy)}
.brand.lw{color:var(--ink);font-weight:700;letter-spacing:.3px}
.brand.lw .sq{width:11px;height:11px;background:var(--navy)}
.brand-pair{display:flex;align-items:center;gap:10px}
.brand-pair .bar{width:1px;height:18px;background:#c9ced3}

/* headers */
.slide-title{position:absolute;left:16px;top:14px;font-family:"Raleway",sans-serif;font-weight:400;font-size:15.5px;letter-spacing:.2px;color:var(--ink);text-transform:uppercase}
.slide-title::after{content:"";position:absolute;left:0;top:23px;width:22px;height:2px;background:var(--navy)}
.head-rule{position:absolute;left:0;right:0;top:38px;height:1px;background:var(--rule)}

/* footer */
.foot{position:absolute;left:8px;right:8px;bottom:5px;height:12px;display:flex;align-items:center;font-size:4px;color:var(--grey)}
.foot .brand{font-size:5px;gap:3px}
.foot .brand .dot{width:8px;height:8px}
.foot .copy{margin-left:8px}
.foot .page{margin-left:auto;margin-right:8px;font-size:4px}
.foot .brand.lw{font-size:6.5px}
.foot .brand.lw .sq{width:7px;height:7px}

/* cover slides */
.cover-logo{position:absolute;left:0;right:0;top:86px;display:flex;justify-content:center}
.cover-logo .brand{font-size:14px}
.cover-logo .brand .dot{width:26px;height:26px}
.big-title{font-family:"Raleway",sans-serif;font-weight:700;color:var(--ink)}
.sub{font-size:5.5px;color:var(--grey)}

.s2 .band{position:absolute;left:0;top:72px;width:120px;height:26px;background:var(--navy);clip-path:polygon(0 0,100% 0,88% 100%,0 100%)}
.s2 .brands{position:absolute;right:8px;top:75px;font-size:8px}
.s2 .brands .brand .dot{width:15px;height:15px}
.s2 .t{position:absolute;right:14px;top:134px;text-align:right}
.s2 .t .big-title{font-size:19px}

.s3 .brands{position:absolute;left:0;right:0;top:54px;display:flex;justify-content:center;font-size:10px}
.s3 .brands .brand .dot{width:19px;height:19px}
.s3 .brands .brand.lw{font-size:13px}
.s3 .line{position:absolute;left:0;right:0;top:133px;height:2px;background:var(--navy)}
.s3 .t{position:absolute;left:0;right:0;top:144px;text-align:center}
.s3 .t .big-title{font-size:19px}

.photo-slide .photo{position:absolute;inset:0}
.photo-slide .t{position:absolute;left:0;right:0;top:80px;text-align:center;color:var(--white)}
.photo-slide .t .big-title{color:var(--white);font-size:19px;text-transform:uppercase;letter-spacing:.3px}
.photo-slide .t .sub{color:var(--white);text-align:right;padding-right:46px;margin-top:2px}
.s4 .photo{background:linear-gradient(160deg,#2c6f9f 0%,#1b5b8f 45%,#123f66 100%)}
.s4 .corner{position:absolute;right:0;bottom:0;width:150px;height:100px;background:var(--white);clip-path:polygon(100% 0,100% 100%,0 100%)}
.s4 .corner-line{position:absolute;right:0;bottom:0;width:152px;height:102px;background:var(--orange);clip-path:polygon(100% 0,100% 2%,2% 100%,0 100%)}
.s4 .brands{position:absolute;right:8px;bottom:8px;font-size:4px}
.s4 .brands .brand .dot{width:7px;height:7px}
.s4 .brands .brand.lw{font-size:5px}
.s5 .photo{background:linear-gradient(150deg,#f58a3c 0%,#ec6c1d 55%,#c9541a 100%)}
.s5 .corner{position:absolute;right:0;bottom:0;width:340px;height:196px;background:var(--green);clip-path:polygon(100% 96%,100% 100%,48% 100%)}
.s5 .top-tri{position:absolute;left:0;top:0;width:130px;height:160px;background:var(--white);clip-path:polygon(0 0,100% 0,0 100%)}
.s5 .tl{position:absolute;left:8px;top:18px;font-size:4.5px}
.s5 .tl .brand .dot{width:9px;height:9px}
.s5 .br{position:absolute;right:8px;bottom:14px}
.s5 .br .brand{color:var(--white);font-size:8px}
.s5 .br .brand .sq{background:var(--white)}

/* roles */
.roles{position:absolute;left:7px;right:7px;top:65px;display:grid;grid-template-columns:repeat(6,1fr);gap:3px}
.role{background:#e4e8ec;height:86px}
.role h4{background:var(--navy);color:var(--white);font-size:3.6px;font-weight:600;padding:2px 3px;height:9px}
.role .ic{width:12px;height:12px;border-radius:50%;border:1px solid var(--navy);margin:4px auto 3px;background:var(--white)}
.role p{font-size:2.8px;line-height:1.35;color:#5a6168;padding:0 3px}

/* chevrons */
.chev{position:absolute;left:36px;top:57px;width:272px;height:30px}
.phase-body{position:absolute;left:38px;top:102px}
.phase-body h5{font-size:7.5px;font-weight:600;margin-bottom:3px}
.phase-body li{list-style:none;font-size:6px;color:#6a7076;line-height:1.55}
.phase-body li::before{content:"•";margin-right:4px;color:var(--navy)}
.phase-body li.sub{padding-left:18px;font-style:italic;color:#8a9096}
.phase-body li.sub::before{content:"";margin:0}
.c-navy{color:var(--navy)}.c-orange{color:var(--orange)}.c-green{color:var(--green)}
.circles{position:absolute;left:60px;top:100px;display:flex;gap:32px}
.circles div{width:53px;height:53px;border-radius:50%;display:flex;align-items:center;justify-content:center;text-align:center;color:var(--white);font-size:4px;font-weight:600}

/* agenda */
.agenda{position:absolute;left:30px;top:58px;display:grid;grid-template-columns:140px 140px;row-gap:14px;column-gap:4px}
.ag{display:flex;gap:6px}
.ag .time{width:27px;height:11px;background:var(--navy);color:var(--white);font-size:3.5px;display:flex;align-items:center;justify-content:center;margin-top:2px}
.ag h6{font-family:"Raleway",sans-serif;font-weight:400;font-size:7px;color:var(--navy)}
.ag p{font-size:2.8px;color:#9aa0a6;line-height:1.3;width:92px}

/* mosaic */
.mosaic{position:absolute;inset:0;display:grid;grid-template-columns:1fr 1fr;grid-template-rows:1fr 1fr 1fr}
.mosaic .txt{padding:6px 20px;font-size:5px;line-height:1.3;color:var(--white)}
.mosaic .ph{background:linear-gradient(135deg,#c9ccd0,#6d7176)}
.mosaic .ph.dark{background:linear-gradient(135deg,#5b6066,#a9adb2)}

/* four columns */
.cols4{position:absolute;left:0;right:0;top:67px;height:98px;display:grid;grid-template-columns:repeat(4,1fr)}
.cols4 > div{padding:14px 6px 0;color:var(--white);text-align:center}
.cols4 .ic{width:14px;height:14px;border:1.2px solid var(--white);border-radius:50%;margin:0 auto 14px}
.cols4 h6{font-size:6px;font-weight:400;margin-bottom:2px}
.cols4 p{font-size:4px;line-height:1.25;text-align:justify}

/* divider */
.divider{position:absolute;left:0;right:0;top:80px;text-align:right;padding-right:32px}
.divider .brands{display:flex;justify-content:flex-end;margin-bottom:14px;margin-right:16px;font-size:7px}
.divider .brands .brand .dot{width:17px;height:17px}
.divider .big-title{font-size:14px;font-weight:800;letter-spacing:.3px}
.divider .sub{color:var(--ink);font-size:5.5px;margin-bottom:5px}
.divider p{font-size:3.6px;text-align:center;margin-left:180px;line-height:1.3;color:#444}

/* text & bullets */
.tb-left{position:absolute;left:20px;top:62px;width:90px}
.tb-left h6{font-size:6px;font-weight:400;margin-bottom:8px}
.tb-left p{font-size:3.6px;color:#9aa0a6;line-height:1.3;margin-bottom:6px}
.tb-grid{position:absolute;left:124px;top:60px;display:grid;grid-template-columns:110px 100px;row-gap:10px}
.tb{display:flex;gap:6px}
.tb i{width:14px;height:14px;border-radius:50%;flex:none}
.tb h6{font-size:6.5px;font-weight:400}
.tb p{font-size:2.8px;color:#9aa0a6;line-height:1.3;width:66px}
</style>
</head>
<body>
<main class="deck">

  <!-- 1 logo cover -->
  <section class="slide">
    <div class="cover-logo"><div class="brand-pair"><span class="brand"><span class="dot"></span>quorbinlab</span></div></div>
  </section>

  <!-- 2 title with band -->
  <section class="slide s2">
    <div class="band"></div>
    <div class="brands brand-pair">
      <span class="brand"><span class="dot"></span>quorbinlab</span><span class="bar"></span>
      <span class="brand lw"><span class="sq"></span>LEDGERWAVE</span>
    </div>
    <div class="t"><div class="big-title">Your Title Goes Here</div><div class="sub">Your Subtitle Goes Here</div></div>
  </section>

  <!-- 3 centred title -->
  <section class="slide s3">
    <div class="brands brand-pair">
      <span class="brand"><span class="dot"></span>quorbinlab</span><span class="bar"></span>
      <span class="brand lw"><span class="sq"></span>LEDGERWAVE</span>
    </div>
    <div class="line"></div>
    <div class="t"><div class="big-title">Your Title Goes Here</div><div class="sub">Your Subtitle Goes Here</div></div>
  </section>

  <!-- 4 blue photo title -->
  <section class="slide photo-slide s4">
    <div class="photo" role="img" aria-label="Photo of an empty modern conference room, blue tinted"></div>
    <div class="corner-line"></div><div class="corner"></div>
    <div class="t"><div class="big-title">Your Title Goes Here</div><div class="sub">Your Subtitle Goes Here</div></div>
    <div class="brands brand-pair"><span class="brand"><span class="dot"></span>quorbinlab</span><span class="brand lw"><span class="sq"></span>LEDGERWAVE</span></div>
  </section>

  <!-- 5 orange photo title -->
  <section class="slide photo-slide s5">
    <div class="photo" role="img" aria-label="Photo of two climbers helping each other on a cliff, orange tinted"></div>
    <div class="top-tri"></div><div class="corner"></div>
    <div class="tl"><span class="brand"><span class="dot"></span>quorbinlab</span></div>
    <div class="t"><div class="big-title">Your Title Goes Here</div><div class="sub">Your Subtitle Goes Here</div></div>
    <div class="br"><span class="brand lw"><span class="sq"></span>LEDGERWAVE</span></div>
  </section>

  <!-- 6 roles -->
  <section class="slide">
    <h2 class="slide-title">Roles &amp; Responsibilities</h2><div class="head-rule"></div>
    <div class="roles">
      <div class="role"><h4>Project Sponsor</h4><div class="ic"></div><p>Overall project champion and vocal leader. Ensures deliverables satisfy goals. Monitors results and reviews performance. Provides facilities.</p></div>
      <div class="role"><h4>Quality Assurance</h4><div class="ic"></div><p>Ensures quality work products. Provides expertise and direction to the team. Monitors overall engagement and manages the QA process.</p></div>
      <div class="role"><h4>Change Management</h4><div class="ic"></div><p>Leads the transition. Assesses impact of changes on the organization and staff. Develops the communication and training plan.</p></div>
      <div class="role"><h4>Steering Committee</h4><div class="ic"></div><p>Made up of senior leadership. Sets project direction and supports the vision. Holds weekly status meetings and resolves issues.</p></div>
      <div class="role"><h4>Project Management</h4><div class="ic"></div><p>Weekly project team status meetings. Reports to the committee. Keeps scope on time and on budget. Mitigates risks.</p></div>
      <div class="role"><h4>Team Leaders</h4><div class="ic"></div><p>Execute the project plan. Identify risks and propose actions. Configure and test systems. Design processes. Weekly team meetings.</p></div>
    </div>
    <footer class="foot"><span class="brand"><span class="dot"></span>quorbinlab</span><span class="copy">© 2017 quorbinlab. All rights reserved</span><span class="page">6</span><span class="brand lw"><span class="sq"></span>LEDGERWAVE</span></footer>
  </section>

  <!-- 7 phase overview -->
  <section class="slide">
    <h2 class="slide-title">Phase One Methodology</h2><div class="head-rule"></div>
    <svg class="chev" viewBox="0 0 280 30" aria-hidden="true">
      <g fill="#eef0f2" stroke="#dfe3e7" stroke-width=".5">
        <polygon points="0,0 52,0 60,15 52,30 0,30"/><polygon points="55,0 107,0 115,15 107,30 55,30 63,15"/><polygon points="110,0 162,0 170,15 162,30 110,30 118,15"/><polygon points="165,0 217,0 225,15 217,30 165,30 173,15"/><polygon points="220,0 272,0 280,15 272,30 220,30 228,15"/>
      </g>
      <g fill="none" stroke-width="1"><circle cx="14" cy="15" r="6" stroke="#1b5b8f"/><circle cx="75" cy="15" r="6" stroke="#f07123"/><circle cx="130" cy="15" r="6" stroke="#6bb23f"/><circle cx="185" cy="15" r="6" stroke="#1b5b8f"/><circle cx="240" cy="15" r="6" stroke="#f07123"/></g>
      <g font-size="3.6" font-family="Open Sans" font-weight="600"><text x="24" y="14" fill="#1b5b8f">Project<tspan x="24" dy="4">Initiation</tspan></text><text x="84" y="14" fill="#f07123">Solution<tspan x="84" dy="4">Design</tspan></text><text x="139" y="14" fill="#6bb23f">Application<tspan x="139" dy="4">Configuration</tspan></text><text x="194" y="14" fill="#1b5b8f">Testing &amp;<tspan x="194" dy="4">Preparation</tspan></text><text x="249" y="14" fill="#f07123">Deployment<tspan x="249" dy="4">&amp; Support</tspan></text></g>
    </svg>
    <div class="circles">
      <div style="background:var(--navy)">Change<br>Management</div>
      <div style="background:var(--green)">User<br>Involvement</div>
      <div style="background:var(--orange)">Program<br>Management</div>
    </div>
    <footer class="foot"><span class="brand"><span class="dot"></span>quorbinlab</span><span class="copy">© 2017 quorbinlab. All rights reserved</span><span class="page">7</span><span class="brand lw"><span class="sq"></span>LEDGERWAVE</span></footer>
  </section>

  <!-- 8 project initiation -->
  <section class="slide">
    <h2 class="slide-title">Phase One Methodology</h2><div class="head-rule"></div>
    <svg class="chev" viewBox="0 0 280 30" aria-hidden="true">
      <g fill="#eef0f2" stroke="#dfe3e7" stroke-width=".5">
        <polygon points="0,0 52,0 60,15 52,30 0,30" fill="#1b5b8f"/><polygon points="55,0 107,0 115,15 107,30 55,30 63,15"/><polygon points="110,0 162,0 170,15 162,30 110,30 118,15"/><polygon points="165,0 217,0 225,15 217,30 165,30 173,15"/><polygon points="220,0 272,0 280,15 272,30 220,30 228,15"/>
      </g>
      <g fill="none" stroke-width="1"><circle cx="14" cy="15" r="6" stroke="#fff"/><circle cx="75" cy="15" r="6" stroke="#f07123"/><circle cx="130" cy="15" r="6" stroke="#6bb23f"/><circle cx="185" cy="15" r="6" stroke="#1b5b8f"/><circle cx="240" cy="15" r="6" stroke="#f07123"/></g>
      <g font-size="3.6" font-family="Open Sans" font-weight="600"><text x="24" y="14" fill="#fff">Project<tspan x="24" dy="4">Initiation</tspan></text><text x="84" y="14" fill="#f07123">Solution<tspan x="84" dy="4">Design</tspan></text><text x="139" y="14" fill="#6bb23f">Application<tspan x="139" dy="4">Configuration</tspan></text><text x="194" y="14" fill="#1b5b8f">Testing &amp;<tspan x="194" dy="4">Preparation</tspan></text><text x="249" y="14" fill="#f07123">Deployment<tspan x="249" dy="4">&amp; Support</tspan></text></g>
    </svg>
    <div class="phase-body">
      <h5 class="c-navy">Project Initiation</h5>
      <ul><li>Conduct Kickoff Meeting</li><li>Finalize and Publish Project Schedule</li><li>Requirements Definition and Design</li><li>Requirements Traceability Matrix (RTM) Signoff</li></ul>
    </div>
    <footer class="foot"><span class="brand"><span class="dot"></span>quorbinlab</span><span class="copy">© 2017 quorbinlab. All rights reserved</span><span class="page">8</span><span class="brand lw"><span class="sq"></span>LEDGERWAVE</span></footer>
  </section>

  <!-- 9 solution design -->
  <section class="slide">
    <h2 class="slide-title">Phase One Methodology</h2><div class="head-rule"></div>
    <svg class="chev" viewBox="0 0 280 30" aria-hidden="true">
      <g fill="#eef0f2" stroke="#dfe3e7" stroke-width=".5">
        <polygon points="0,0 52,0 60,15 52,30 0,30"/><polygon points="55,0 107,0 115,15 107,30 55,30 63,15" fill="#f07123"/><polygon points="110,0 162,0 170,15 162,30 110,30 118,15"/><polygon points="165,0 217,0 225,15 217,30 165,30 173,15"/><polygon points="220,0 272,0 280,15 272,30 220,30 228,15"/>
      </g>
      <g fill="none" stroke-width="1"><circle cx="14" cy="15" r="6" stroke="#1b5b8f"/><circle cx="75" cy="15" r="6" stroke="#fff"/><circle cx="130" cy="15" r="6" stroke="#6bb23f"/><circle cx="185" cy="15" r="6" stroke="#1b5b8f"/><circle cx="240" cy="15" r="6" stroke="#f07123"/></g>
      <g font-size="3.6" font-family="Open Sans" font-weight="600"><text x="24" y="14" fill="#1b5b8f">Project<tspan x="24" dy="4">Initiation</tspan></text><text x="84" y="14" fill="#fff">Solution<tspan x="84" dy="4">Design</tspan></text><text x="139" y="14" fill="#6bb23f">Application<tspan x="139" dy="4">Configuration</tspan></text><text x="194" y="14" fill="#1b5b8f">Testing &amp;<tspan x="194" dy="4">Preparation</tspan></text><text x="249" y="14" fill="#f07123">Deployment<tspan x="249" dy="4">&amp; Support</tspan></text></g>
    </svg>
    <div class="phase-body">
      <h5 class="c-orange">Solution Design</h5>
      <ul><li>Map and Gap Against RTM</li><li>Identify Solutions for Gaps</li><li class="sub">Custom Development</li><li class="sub">Phase Two Initiative</li><li class="sub">Business Process Change</li><li>Business Flow Recommendation</li></ul>
    </div>
    <footer class="foot"><span class="brand"><span class="dot"></span>quorbinlab</span><span class="copy">© 2017 quorbinlab. All rights reserved</span><span class="page">9</span><span class="brand lw"><span class="sq"></span>LEDGERWAVE</span></footer>
  </section>

  <!-- 10 application configuration -->
  <section class="slide">
    <h2 class="slide-title">Phase One Methodology</h2><div class="head-rule"></div>
    <svg class="chev" viewBox="0 0 280 30" aria-hidden="true">
      <g fill="#eef0f2" stroke="#dfe3e7" stroke-width=".5">
        <polygon points="0,0 52,0 60,15 52,30 0,30"/><polygon points="55,0 107,0 115,15 107,30 55,30 63,15"/><polygon points="110,0 162,0 170,15 162,30 110,30 118,15" fill="#6bb23f"/><polygon points="165,0 217,0 225,15 217,30 165,30 173,15"/><polygon points="220,0 272,0 280,15 272,30 220,30 228,15"/>
      </g>
      <g fill="none" stroke-width="1"><circle cx="14" cy="15" r="6" stroke="#1b5b8f"/><circle cx="75" cy="15" r="6" stroke="#f07123"/><circle cx="130" cy="15" r="6" stroke="#fff"/><circle cx="185" cy="15" r="6" stroke="#1b5b8f"/><circle cx="240" cy="15" r="6" stroke="#f07123"/></g>
      <g font-size="3.6" font-family="Open Sans" font-weight="600"><text x="24" y="14" fill="#1b5b8f">Project<tspan x="24" dy="4">Initiation</tspan></text><text x="84" y="14" fill="#f07123">Solution<tspan x="84" dy="4">Design</tspan></text><text x="139" y="14" fill="#fff">Application<tspan x="139" dy="4">Configuration</tspan></text><text x="194" y="14" fill="#1b5b8f">Testing &amp;<tspan x="194" dy="4">Preparation</tspan></text><text x="249" y="14" fill="#f07123">Deployment<tspan x="249" dy="4">&amp; Support</tspan></text></g>
    </svg>
    <div class="phase-body">
      <h5 class="c-green">Application Configuration</h5>
      <ul><li>System Setup</li><li>Extended Prototyping</li><li>Develop Test Scripts</li><li>Initiate Data Cleansing and Conversion Routines</li></ul>
    </div>
    <footer class="foot"><span class="brand"><span class="dot"></span>quorbinlab</span><span class="copy">© 2017 quorbinlab. All rights reserved</span><span class="page">10</span><span class="brand lw"><span class="sq"></span>LEDGERWAVE</span></footer>
  </section>

  <!-- 11 testing -->
  <section class="slide">
    <h2 class="slide-title">Phase One Methodology</h2><div class="head-rule"></div>
    <svg class="chev" viewBox="0 0 280 30" aria-hidden="true">
      <g fill="#eef0f2" stroke="#dfe3e7" stroke-width=".5">
        <polygon points="0,0 52,0 60,15 52,30 0,30"/><polygon points="55,0 107,0 115,15 107,30 55,30 63,15"/><polygon points="110,0 162,0 170,15 162,30 110,30 118,15"/><polygon points="165,0 217,0 225,15 217,30 165,30 173,15" fill="#1b5b8f"/><polygon points="220,0 272,0 280,15 272,30 220,30 228,15"/>
      </g>
      <g fill="none" stroke-width="1"><circle cx="14" cy="15" r="6" stroke="#1b5b8f"/><circle cx="75" cy="15" r="6" stroke="#f07123"/><circle cx="130" cy="15" r="6" stroke="#6bb23f"/><circle cx="185" cy="15" r="6" stroke="#fff"/><circle cx="240" cy="15" r="6" stroke="#f07123"/></g>
      <g font-size="3.6" font-family="Open Sans" font-weight="600"><text x="24" y="14" fill="#1b5b8f">Project<tspan x="24" dy="4">Initiation</tspan></text><text x="84" y="14" fill="#f07123">Solution<tspan x="84" dy="4">Design</tspan></text><text x="139" y="14" fill="#6bb23f">Application<tspan x="139" dy="4">Configuration</tspan></text><text x="194" y="14" fill="#fff">Testing &amp;<tspan x="194" dy="4">Preparation</tspan></text><text x="249" y="14" fill="#f07123">Deployment<tspan x="249" dy="4">&amp; Support</tspan></text></g>
    </svg>
    <div class="phase-body">
      <h5 class="c-navy">Testing &amp; Preparation</h5>
      <ul><li>Unit Testing – Individual modules/functions</li><li>Integration Testing – End-to-End Flow (Order to Cash)</li><li>User Acceptance Testing – Mock Go-Live</li><li>Full Life Cycle Simulations</li><li>End User Training</li></ul>
    </div>
    <footer class="foot"><span class="brand"><span class="dot"></span>quorbinlab</span><span class="copy">© 2017 quorbinlab. All rights reserved</span><span class="page">11</span><span class="brand lw"><span class="sq"></span>LEDGERWAVE</span></footer>
  </section>

  <!-- 12 deployment -->
  <section class="slide">
    <h2 class="slide-title">Phase One Methodology</h2><div class="head-rule"></div>
    <svg class="chev" viewBox="0 0 280 30" aria-hidden="true">
      <g fill="#eef0f2" stroke="#dfe3e7" stroke-width=".5">
        <polygon points="0,0 52,0 60,15 52,30 0,30"/><polygon points="55,0 107,0 115,15 107,30 55,30 63,15"/><polygon points="110,0 162,0 170,15 162,30 110,30 118,15"/><polygon points="165,0 217,0 225,15 217,30 165,30 173,15"/><polygon points="220,0 272,0 280,15 272,30 220,30 228,15" fill="#f07123"/>
      </g>
      <g fill="none" stroke-width="1"><circle cx="14" cy="15" r="6" stroke="#1b5b8f"/><circle cx="75" cy="15" r="6" stroke="#f07123"/><circle cx="130" cy="15" r="6" stroke="#6bb23f"/><circle cx="185" cy="15" r="6" stroke="#1b5b8f"/><circle cx="240" cy="15" r="6" stroke="#fff"/></g>
      <g font-size="3.6" font-family="Open Sans" font-weight="600"><text x="24" y="14" fill="#1b5b8f">Project<tspan x="24" dy="4">Initiation</tspan></text><text x="84" y="14" fill="#f07123">Solution<tspan x="84" dy="4">Design</tspan></text><text x="139" y="14" fill="#6bb23f">Application<tspan x="139" dy="4">Configuration</tspan></text><text x="194" y="14" fill="#1b5b8f">Testing &amp;<tspan x="194" dy="4">Preparation</tspan></text><text x="249" y="14" fill="#fff">Deployment<tspan x="249" dy="4">&amp; Support</tspan></text></g>
    </svg>
    <div class="phase-body">
      <h5 class="c-orange">Deployment &amp; Support</h5>
      <ul><li>Setup Production Environment</li><li>Convert Live Data</li><li>GO-LIVE!</li><li>Post Go-Live Support</li><li>Project Closeout</li></ul>
    </div>
    <footer class="foot"><span class="brand"><span class="dot"></span>quorbinlab</span><span class="copy">© 2017 quorbinlab. All rights reserved</span><span class="page">12</span><span class="brand lw"><span class="sq"></span>LEDGERWAVE</span></footer>
  </section>

  <!-- 13 five key areas -->
  <section class="slide">
    <h2 class="slide-title">Five Key Areas of User Adoption</h2><div class="head-rule"></div>
    <svg style="position:absolute;left:102px;top:46px" width="140" height="140" viewBox="0 0 140 140" aria-label="Cycle of five adoption areas">
      <g fill="none" stroke-width="22" transform="rotate(-90 70 70)">
        <circle cx="70" cy="70" r="46" stroke="#1b5b8f" stroke-dasharray="57 232" stroke-dashoffset="0"/>
        <circle cx="70" cy="70" r="46" stroke="#6bb23f" stroke-dasharray="55 234" stroke-dashoffset="-58"/>
        <circle cx="70" cy="70" r="46" stroke="#f07123" stroke-dasharray="55 234" stroke-dashoffset="-115"/>
        <circle cx="70" cy="70" r="46" stroke="#1b5b8f" stroke-dasharray="55 234" stroke-dashoffset="-172"/>
        <circle cx="70" cy="70" r="46" stroke="#6bb23f" stroke-dasharray="60 229" stroke-dashoffset="-229"/>
      </g>
      <circle cx="70" cy="70" r="33" fill="#fff"/>
      <circle cx="70" cy="70" r="10" fill="none" stroke="#1b5b8f" stroke-width="1.5"/>
      <g fill="#fff" stroke="#ccc" stroke-width=".6"><circle cx="98" cy="40" r="8"/><circle cx="114" cy="86" r="8"/><circle cx="70" cy="116" r="8"/><circle cx="26" cy="86" r="8"/><circle cx="42" cy="40" r="8"/></g>
      <g font-size="4" fill="#fff" font-family="Open Sans"><text x="76" y="30">Communication</text><text x="116" y="66" transform="rotate(80 116 66)">Training</text><text x="74" y="131">Support</text><text x="14" y="60" transform="rotate(75 14 60)">Measurement</text><text x="30" y="34" transform="rotate(-55 30 34)">Alignment</text></g>
    </svg>
    <footer class="foot"><span class="brand"><span class="dot"></span>quorbinlab</span><span class="copy">© 2017 quorbinlab. All rights reserved</span><span class="page">13</span><span class="brand lw"><span class="sq"></span>LEDGERWAVE</span></footer>
  </section>

  <!-- 14 agenda -->
  <section class="slide">
    <h2 class="slide-title">Our Agenda</h2><div class="head-rule"></div>
    <div class="agenda">
      <div class="ag"><span class="time">10:00 | ◷</span><div><h6>Agenda One</h6><p>Short welcome and team intros to open the session today.</p></div></div>
      <div class="ag"><span class="time">13:00 | ◷</span><div><h6>Agenda Four</h6><p>Walk through the proposed plan and main project phases.</p></div></div>
      <div class="ag"><span class="time">11:00 | ◷</span><div><h6>Agenda Two</h6><p>Review your goals, current systems and key pain points.</p></div></div>
      <div class="ag"><span class="time">14:00 | ◷</span><div><h6>Agenda Five</h6><p>Discuss timing, budget range and the people involved.</p></div></div>
      <div class="ag"><span class="time">12:00 | ◷</span><div><h6>Agenda Three</h6><p>Live product demo focused on your daily business flows.</p></div></div>
      <div class="ag"><span class="time">15:00 | ◷</span><div><h6>Agenda Six</h6><p>Open questions, agreed next steps and a follow up date.</p></div></div>
    </div>
    <footer class="foot"><span class="brand"><span class="dot"></span>quorbinlab</span><span class="copy">© 2017 quorbinlab. All rights reserved</span><span class="page">14</span><span class="brand lw"><span class="sq"></span>LEDGERWAVE</span></footer>
  </section>

  <!-- 15 mosaic -->
  <section class="slide">
    <div class="mosaic">
      <div class="txt" style="background:var(--navy)">We help growing firms run finance, sales and operations on one cloud platform, with a team that stays with you from kickoff to go-live and well beyond it.</div>
      <div class="ph" role="img" aria-label="Photo of a business handshake"></div>
      <div class="ph dark" role="img" aria-label="Photo of hands working with papers and a laptop"></div>
      <div class="txt" style="background:var(--orange)">Our consultants pair deep product skill with real industry experience, so every setup fits how your people already work instead of forcing new habits on them.</div>
      <div class="txt" style="background:var(--green)">After launch we keep tuning your system, training new users and adding features as the business grows, so the platform keeps paying off year after year.</div>
      <div class="ph" role="img" aria-label="Photo of a hand touching a digital screen"></div>
    </div>
  </section>

  <!-- 16 four columns -->
  <section class="slide">
    <h2 class="slide-title">Your Title Here</h2><div class="head-rule"></div>
    <div class="cols4">
      <div style="background:#111"><div class="ic"></div><h6>Heading Here</h6><p>Short supporting text for this point goes here and explains the idea in a line or two for the reader.</p></div>
      <div style="background:var(--navy)"><div class="ic"></div><h6>Heading Here</h6><p>Short supporting text for this point goes here and explains the idea in a line or two for the reader.</p></div>
      <div style="background:var(--orange)"><div class="ic"></div><h6>Heading Here</h6><p>Short supporting text for this point goes here and explains the idea in a line or two for the reader.</p></div>
      <div style="background:var(--green)"><div class="ic"></div><h6>Heading Here</h6><p>Short supporting text for this point goes here and explains the idea in a line or two for the reader.</p></div>
    </div>
    <footer class="foot"><span class="brand"><span class="dot"></span>quorbinlab</span><span class="copy">© 2017 quorbinlab. All rights reserved</span><span class="page">16</span><span class="brand lw"><span class="sq"></span>LEDGERWAVE</span></footer>
  </section>

  <!-- 17 divider -->
  <section class="slide">
    <div class="divider">
      <div class="brands brand-pair"><span class="brand"><span class="dot"></span>quorbinlab</span></div>
      <div class="big-title">DIVIDER PAGE</div>
      <div class="sub">Subtitle Here</div>
      <p>A short line of intro text for the next section of the deck goes here, kept to a few brief lines so it reads well.</p>
    </div>
  </section>

  <!-- 18 text & bullets -->
  <section class="slide">
    <h2 class="slide-title">Text &amp; Bullet Area</h2><div class="head-rule"></div>
    <div class="tb-left">
      <h6>Heading Goes Here</h6>
      <p>Intro copy for this slide sits here and gives the main point in a few short lines of plain text.</p>
      <p>A second short paragraph adds detail and backs up the heading above it.</p>
      <p>A third note closes the block with a simple takeaway for the room.</p>
    </div>
    <div class="tb-grid">
      <div class="tb"><i style="background:var(--navy)"></i><div><h6 class="c-navy">Your Text Here</h6><p>Brief note that supports this item.</p></div></div>
      <div class="tb"><i style="background:var(--orange)"></i><div><h6 class="c-orange">Your Text Here</h6><p>Brief note that supports this item.</p></div></div>
      <div class="tb"><i style="background:var(--orange)"></i><div><h6 class="c-orange">Your Text Here</h6><p>Brief note that supports this item.</p></div></div>
      <div class="tb"><i style="background:var(--green)"></i><div><h6 class="c-green">Your Text Here</h6><p>Brief note that supports this item.</p></div></div>
      <div class="tb"><i style="background:var(--green)"></i><div><h6 class="c-green">Your Text Here</h6><p>Brief note that supports this item.</p></div></div>
      <div class="tb"><i style="background:var(--navy)"></i><div><h6 class="c-navy">Your Text Here</h6><p>Brief note that supports this item.</p></div></div>
      <div class="tb"><i style="background:var(--navy)"></i><div><h6 class="c-navy">Your Text Here</h6><p>Brief note that supports this item.</p></div></div>
      <div class="tb"><i style="background:var(--orange)"></i><div><h6 class="c-orange">Your Text Here</h6><p>Brief note that supports this item.</p></div></div>
    </div>
    <footer class="foot"><span class="brand"><span class="dot"></span>quorbinlab</span><span class="copy">© 2017 quorbinlab. All rights reserved</span><span class="page">18</span><span class="brand lw"><span class="sq"></span>LEDGERWAVE</span></footer>
  </section>

</main>
</body>
</html>
```